Business Card Design Project

Dorran
Sales Manager

38700 Pellham Ave, Suite 415
Irvine, CA 92604

Tel: 626-555-0147
Fax: 888-555-0162
E-mail: dorran@plovetrix.com

Target Market(s)

We are the distributor and wholesaler, the business card design want to show we are a strong company.

Industry/Entity Type

Business

Colors

Designer to choose colors to be used in the design.

```html
<!DOCTYPE html>
<html lang="en">
<head>
<meta charset="utf-8">
<title>Plovetrix Business Card</title>
<link rel="stylesheet" href="https://fonts.googleapis.com/css2?family=Open+Sans:wght@400;600&display=swap">
<style>
  :root {
    --backdrop: #e9ebe8;
    --card: #ffffff;
    --green-deep: #2f7a38;
    --green-light: #8cc63f;
    --ink: #333333;
    --ink-soft: #555555;
    --on-green: #ffffff;
  }
  * { margin: 0; padding: 0; box-sizing: border-box; }
  html, body {
    width: 1200px; height: 900px; overflow: hidden;
    background: var(--backdrop);
    font-family: "Open Sans", Arial, sans-serif;
  }
  .canvas {
    position: relative; width: 1200px; height: 900px;
    display: flex; align-items: center; justify-content: center; gap: 40px;
  }
  .card {
    position: relative; width: 540px; height: 310px;
    background: var(--card); border-radius: 24px; overflow: hidden;
    box-shadow: 0 6px 18px rgba(0,0,0,0.12);
  }
  .card-swoosh { position: absolute; inset: 0; width: 100%; height: 100%; }
  .swoosh-light { fill: var(--green-light); }
  .swoosh-deep { fill: var(--green-deep); }

  .brand {
    position: absolute; display: flex; align-items: center; gap: 10px;
    color: var(--green-deep); font-weight: 600;
  }
  .brand-dot { border-radius: 50%; background: var(--green-light); }
  .front .brand { left: 38px; top: 58px; font-size: 30px; }
  .front .brand-dot { width: 14px; height: 14px; }
  .back .brand { left: 50%; top: 50%; transform: translate(-50%, -50%); font-size: 40px; }
  .back .brand-dot { width: 18px; height: 18px; }

  .holder { position: absolute; right: 56px; top: 52px; text-align: right; }
  .holder-name { font-size: 17px; font-weight: 600; letter-spacing: 0.5px; color: var(--ink); text-transform: uppercase; }
  .holder-role { font-size: 13px; color: var(--ink-soft); margin-top: 2px; }

  .contact {
    position: absolute; right: 22px; top: 160px;
    list-style: none; color: var(--on-green); font-size: 11.5px; text-align: right;
  }
  .contact li { display: flex; align-items: center; justify-content: flex-end; gap: 8px; line-height: 1.35; margin-bottom: 5px; }
  .contact svg { width: 11px; height: 11px; flex: none; fill: var(--on-green); }
</style>
</head>
<body>
<main class="canvas">
  <section class="card front">
    <svg class="card-swoosh" viewBox="0 0 540 310" preserveAspectRatio="none" aria-hidden="true">
      <path class="swoosh-light" d="M0,168 C190,205 390,185 540,78 L540,310 L0,310Z"/>
      <path class="swoosh-deep" d="M0,186 C200,224 400,202 540,100 L540,310 L0,310Z"/>
    </svg>
    <div class="brand"><span class="brand-dot"></span>Plovetrix</div>
    <div class="holder">
      <p class="holder-name">Dorran Halvey</p>
      <p class="holder-role">Sales Manager</p>
    </div>
    <ul class="contact">
      <li><span>38700 Pellham Ave, Suite 415<br>Irvine, CA 92604</span>
        <svg viewBox="0 0 12 12"><path d="M6 0a4 4 0 0 0-4 4c0 3 4 8 4 8s4-5 4-8a4 4 0 0 0-4-4zm0 5.5a1.5 1.5 0 1 1 0-3 1.5 1.5 0 0 1 0 3z"/></svg></li>
      <li><span>Tel: 626-555-0147</span>
        <svg viewBox="0 0 12 12"><path d="M2.5 0.5l2 2.5-1 1.5c.8 1.6 1.9 2.7 3.5 3.5l1.5-1 2.5 2-1 2.5C5 11 1 7 0 2.5z"/></svg></li>
      <li><span>Fax: 888-555-0162</span>
        <svg viewBox="0 0 12 12"><path d="M3 0h6v3H3zM1 4h10v6H9v2H3v-2H1zM4 8v3h4V8z"/></svg></li>
      <li><span>dorran@plovetrix.com</span>
        <svg viewBox="0 0 12 12"><path d="M0 2h12v8H0zm1 1v.5l5 3.5 5-3.5V3z"/></svg></li>
      <li><span>www.plovetrix.com</span>
        <svg viewBox="0 0 12 12"><circle cx="6" cy="6" r="5.5"/></svg></li>
    </ul>
  </section>

  <section class="card back">
    <div class="brand"><span class="brand-dot"></span>Plovetrix</div>
  </section>
</main>
</body>
</html>
```